" Atuamos como laboratório de análises clínicas, oferecendo exames laboratoriais para diagnóstico e prevenção de doenças. Nosso atendimento é feito tanto para pacientes particulares quanto por convênios, com coleta realizada em nossa unidade por profissionais qualificados. Os resultados são disponibilizados de forma rápida, podendo ser acessados online ou retirados presencialmente. Trabalhamos com foco em qualidade, confiabilidade e atendimento humanizado. "

```html
<!DOCTYPE html>
<html lang="pt-BR">
<head>
<meta charset="utf-8">
<title>Vitalis Lab – Cartão Fidelidade</title>
<link href="https://fonts.googleapis.com/css2?family=Montserrat:wght@400;500;600;700&display=swap" rel="stylesheet">
<style>
  :root{
    --bg:#3b3939;
    --green:#22a55a;
    --green-dark:#1c8f4d;
    --white:#ffffff;
    --paper:#f4f6f5;
    --ink:#4b5a52;
    --stamp:#b9d9c5;
  }
  *{margin:0;padding:0;box-sizing:border-box}
  html,body{width:1200px;height:1200px;overflow:hidden}
  body{background:var(--bg);font-family:'Montserrat',sans-serif;display:flex;flex-direction:column;align-items:center;justify-content:center;gap:70px}
  .card{width:780px;height:446px;border-radius:26px;position:relative;overflow:hidden;box-shadow:0 18px 40px rgba(0,0,0,.35)}
  /* back: loyalty stamps */
  .card--back{background:linear-gradient(135deg,var(--white) 0%,var(--paper) 100%)}
  .back__brand{position:absolute;left:70px;top:78px;display:flex;align-items:center;gap:14px}
  .brand-dot{width:26px;height:26px;border-radius:50%;background:var(--green)}
  .back__name{font-size:36px;font-weight:700;color:var(--green);letter-spacing:.5px}
  .back__tag{position:absolute;left:110px;top:124px;font-size:13px;color:var(--ink);letter-spacing:.4px}
  .stamps{position:absolute;left:360px;top:70px;display:grid;grid-template-columns:repeat(5,56px);gap:26px 30px}
  .stamp{width:56px;height:56px;border-radius:50%;border:2px solid var(--stamp)}
  .back__rule{position:absolute;left:360px;right:70px;top:258px;height:3px;background:var(--green)}
  .back__contact{position:absolute;left:70px;right:70px;bottom:56px;display:flex;justify-content:space-between;font-size:14px;color:var(--ink)}
  /* front: green */
  .card--front{background:var(--green)}
  .front__divider{position:absolute;left:330px;top:60px;bottom:60px;width:2px;background:rgba(255,255,255,.75)}
  .front__label{position:absolute;left:60px;top:196px;font-size:19px;font-weight:600;letter-spacing:1.5px;color:var(--white)}
  .front__label-rule{position:absolute;left:60px;width:230px;top:236px;height:2px;background:rgba(255,255,255,.75)}
  .front__brand{position:absolute;left:380px;top:160px;display:flex;align-items:center;gap:18px}
  .front__brand .brand-dot{width:40px;height:40px;background:var(--white)}
  .front__name{font-size:58px;font-weight:700;color:var(--white);letter-spacing:.5px}
  .front__tag{position:absolute;left:438px;top:250px;font-size:18px;color:var(--white);letter-spacing:.4px}
</style>
</head>
<body>
  <section class="card card--back">
    <div class="back__brand"><span class="brand-dot"></span><span class="back__name">Vitalis Lab</span></div>
    <p class="back__tag">Laboratório de Análises Clínicas</p>
    <div class="stamps">
      <span class="stamp"></span><span class="stamp"></span><span class="stamp"></span><span class="stamp"></span><span class="stamp"></span>
      <span class="stamp"></span><span class="stamp"></span><span class="stamp"></span><span class="stamp"></span><span class="stamp"></span>
    </div>
    <div class="back__rule"></div>
    <div class="back__contact">
      <span>(61) 3200-4500</span>
      <span>contato@vitalislab.com.br</span>
      <span>vitalislab.com.br</span>
    </div>
  </section>

  <section class="card card--front">
    <p class="front__label">CARTÃO FIDELIDADE</p>
    <div class="front__label-rule"></div>
    <div class="front__divider"></div>
    <div class="front__brand"><span class="brand-dot"></span><span class="front__name">Vitalis Lab</span></div>
    <p class="front__tag">Laboratório de Análises Clínicas</p>
  </section>
</body>
</html>
```